We need visit card and a letter paper for our website. thx

We have a beauty clinic in Switzerland.
https://wolkenbachtal.ch
We need a visit card.

Requirements
Must have
• see colors on website

```html
<!DOCTYPE html>
<html lang="de">
<head>
<meta charset="utf-8">
<title>Wolkenbachtal – Visitenkarte</title>
<link href="https://fonts.googleapis.com/css2?family=Marcellus&family=Montserrat:wght@400;500;600&display=swap" rel="stylesheet">
<style>
  :root {
    --stage: #141414;
    --card: #1c1c1c;
    --white: #f4f4f4;
    --grey: #8a8a8a;
    --pink: #c8437b;
  }
  * { box-sizing: border-box; margin: 0; padding: 0; }
  html, body { width: 1200px; height: 895px; overflow: hidden; }
  body {
    background: var(--stage);
    display: flex;
    flex-direction: column;
    align-items: center;
    justify-content: center;
    gap: 32px;
    font-family: "Montserrat", sans-serif;
    color: var(--white);
  }
  .card {
    width: 700px;
    height: 400px;
    background: var(--card);
    position: relative;
    box-shadow: 0 10px 30px rgba(0,0,0,.6);
  }

  /* Front */
  .card-front {
    display: flex;
    flex-direction: column;
    align-items: center;
    justify-content: center;
  }
  .brand-name {
    font-family: "Marcellus", serif;
    font-size: 54px;
    letter-spacing: 1px;
    color: var(--grey);
    line-height: 1;
    white-space: nowrap;
  }
  .card-front .website {
    position: absolute;
    bottom: 64px;
    left: 0; right: 0;
    text-align: center;
    font-size: 21px;
    font-weight: 500;
    letter-spacing: .5px;
  }
  .website .domain { color: var(--pink); font-weight: 600; }

  /* Back */
  .card-back {
    display: flex;
    align-items: center;
    padding: 0 44px 0 48px;
  }
  .card-back .brand {
    flex: 1;
    display: flex;
    justify-content: center;
    padding-top: 120px;
    padding-right: 36px;
  }
  .card-back .brand-name { color: var(--white); font-size: 34px; letter-spacing: .5px; }

  .contact {
    width: 290px;
    flex: none;
    font-size: 14px;
    line-height: 1.35;
    padding-bottom: 40px;
  }
  .contact .person {
    font-family: "Marcellus", serif;
    color: var(--pink);
    font-size: 22px;
    letter-spacing: .5px;
  }
  .contact .role { margin-bottom: 18px; }
  .contact .address { margin-bottom: 16px; }
  .contact .channels { list-style: none; }
  .contact .channels li {
    display: flex;
    align-items: center;
    gap: 10px;
    margin-bottom: 2px;
  }
  .channels svg { width: 13px; height: 13px; flex: none; }
</style>
</head>
<body>

<section class="card card-front">
  <div class="brand-name">Wolkenbachtal</div>
  <p class="website">www.<span class="domain">wolkenbachtal</span>.ch</p>
</section>

<section class="card card-back">
  <div class="brand">
    <div class="brand-name">Wolkenbachtal</div>
  </div>
  <div class="contact">
    <p class="person">DR. LENA MARBACH</p>
    <p class="role">FÄ für Plastische Chirurgie</p>
    <p class="address">Talweg 24<br>7099 Bergwil, Schweiz</p>
    <ul class="channels">
      <li>
        <svg viewBox="0 0 16 16" aria-hidden="true"><path fill="#c8437b" d="M2 5c0-2 3-3 6-3s6 1 6 3v1h-3V5H5v1H2zM4 7h8l2 6H2zm4 1.5a2 2 0 1 0 0 4 2 2 0 0 0 0-4z"/></svg>
        +41 (0) 800 55 20 30
      </li>
      <li>
        <svg viewBox="0 0 16 16" aria-hidden="true"><rect x="1.5" y="3.5" width="13" height="9" fill="none" stroke="#c8437b" stroke-width="1.5"/><path d="M1.5 3.5 8 9l6.5-5.5" fill="none" stroke="#c8437b" stroke-width="1.5"/></svg>
        hallo@wolkenbachtal.ch
      </li>
      <li>
        <svg viewBox="0 0 16 16" aria-hidden="true"><g fill="none" stroke="#c8437b" stroke-width="1.3"><circle cx="8" cy="8" r="6.5"/><ellipse cx="8" cy="8" rx="3" ry="6.5"/><path d="M1.5 8h13M2.5 5h11M2.5 11h11"/></g></svg>
        www.wolkenbachtal.ch
      </li>
    </ul>
  </div>
</section>

</body>
</html>
```